Brisk Lark Delivery Service Wordpress design

My client is a delivery service whose motto is "ON TIME, ON ROUTE, EVERY LOAD." Their colors are red, white and blue. They use Voyara vans and box vans - NO semi tractors. They like this Website design www.kwuzo.com, but I would like to see some designs that make them stand out. Attached is their new logo.

Target Market(s)

Businesses who use delivery services in town and anyone needing freight picked up or transported in the United States.

Industry/Entity Type

Delivery Service

Number of Pages Required

1 page

Font styles to use
Sans Serif

Colors
ec1f27
0455a3
ffffff

Requirements
Must have
• We need a Wordpress design with sliders that incorporates their new logo and the motto "ON TIME, ON ROUTE, EVERY LOAD" Their corporate colors are red, white and blue. They only use voyara vans and box vans.
Nice to have
• Please use your creativity to come up with a unique design for this delivery service.
Should not have
• NO SEMI TRACTOR TRAILERS

```html
<!DOCTYPE html>
<html lang="en">
<head>
<meta charset="utf-8">
<title>Brisk Lark Express Delivery</title>
<link rel="stylesheet" href="https://fonts.googleapis.com/css2?family=Open+Sans:ital,wght@0,400;0,600;0,700;0,800;1,700&family=Roboto+Condensed:wght@700&display=swap">
<style>
:root{
  --red:#e41f2a;
  --red-dark:#c81821;
  --navy:#1d1a6b;
  --blue:#0b73c9;
  --ink:#333333;
  --text:#444444;
  --page:#e9e9e9;
  --panel:#ededed;
  --white:#ffffff;
  --footer:#333333;
  --black:#111111;
  --line:#d6d6d6;
}
*{margin:0;padding:0;box-sizing:border-box}
html,body{width:1200px;height:2744px;overflow:hidden}
body{background:var(--page);font-family:"Open Sans",Arial,sans-serif;color:var(--text);position:relative}
.page{position:absolute;left:15px;top:15px;width:1170px;height:2710px;background:var(--white)}
section,header,nav,footer{position:absolute;left:0;width:1170px}
.abs{position:absolute}

/* header */
.site-header{top:0;height:140px;background:#f7f7f7}
.brand{position:absolute;display:flex;align-items:center;gap:12px}
.brand-name{font-weight:800;font-size:27px;color:var(--navy);letter-spacing:-.3px;white-space:nowrap}
.brand-dot{width:44px;height:44px;border-radius:50%;background:var(--navy);flex:none}
.site-header .brand{left:31px;top:44px}
.motto-band{left:713px;top:0;width:457px;height:40px;background:var(--navy);clip-path:polygon(0 0,100% 0,100% 100%,22px 100%);color:var(--white);font-weight:700;font-size:17px;letter-spacing:1.4px;line-height:40px;padding-left:46px;white-space:nowrap}
.phone-icon{left:872px;top:60px;width:55px;height:55px;border:3px solid var(--ink);border-radius:50%;display:flex;align-items:center;justify-content:center}
.phone-number{left:940px;top:68px;font-size:29px;font-weight:700;color:var(--ink);letter-spacing:.5px}

/* nav */
.main-nav{top:140px;height:46px;background:var(--red)}
.main-nav a{position:absolute;top:0;height:46px;line-height:46px;color:var(--white);text-decoration:none;font-family:"Roboto Condensed",Arial,sans-serif;font-weight:700;font-size:16px}
.main-nav a.active{background:var(--navy);width:95px;text-align:center}

/* hero */
.hero{top:186px;height:604px}
.hero-photo{position:absolute;inset:0;background:linear-gradient(100deg,#cfd3d3 0%,#8d8c87 22%,#b49a78 38%,#e4e4e2 58%,#f2f2f1 74%,#9aa29b 100%)}
.slide-arrow{position:absolute;top:252px;width:52px;height:52px;background:var(--red);display:flex;align-items:center;justify-content:center}
.slide-arrow.prev{left:0}
.slide-arrow.next{right:0}
.quote-card{left:717px;top:124px;width:340px;height:328px;background:var(--white);box-shadow:0 2px 10px rgba(0,0,0,.25)}
.quote-head{left:704px;top:148px;width:366px;height:51px;background:var(--blue);color:var(--white);font-weight:700;font-size:21px;text-align:center;line-height:51px;box-shadow:0 2px 4px rgba(0,0,0,.25)}
.field{left:737px;width:302px;height:36px;border:1px solid #cfcfcf;background:#f1f1f1;display:flex;align-items:center}
.field .icon{width:40px;height:34px;background:#dcdcdc;display:flex;align-items:center;justify-content:center;border-right:1px solid #cfcfcf}
.field span{font-size:13px;font-weight:600;color:#333;padding-left:12px;flex:1}
.field .caret{width:34px;height:34px;border-left:1px solid #cfcfcf;display:flex;align-items:center;justify-content:center;flex:none;padding:0}
.quote-btn{left:787px;top:406px;width:201px;height:29px;background:var(--navy);color:var(--white);font-size:14px;font-weight:700;text-align:center;line-height:29px}
.slider-dots{display:flex;gap:6px}
.slider-dots i{width:12px;height:12px;border-radius:50%;background:var(--white);border:1px solid #999}
.slider-dots i.on{background:var(--red);border-color:var(--red)}
.hero .slider-dots{position:absolute;left:558px;top:577px}

/* headings */
.section-title{position:absolute;left:0;width:1170px;top:62px;text-align:center;font-size:25px;font-weight:600;color:var(--ink)}
.divider{position:absolute;left:86px;top:110px;width:997px;height:18px}
.divider::before,.divider::after{content:"";position:absolute;top:9px;width:448px;height:1px;background:var(--line)}
.divider::before{left:0}
.divider::after{right:0}
.divider i{position:absolute;left:490px;top:0;width:18px;height:18px;border-radius:50%;background:var(--navy)}

/* welcome */
.welcome{top:790px;height:554px;background:var(--white)}
.welcome-copy{left:68px;top:186px;width:561px;font-size:14px;line-height:20.7px;color:var(--text)}
.welcome-copy p{margin-bottom:20px}
.video-frame{left:668px;top:188px;width:435px;height:306px;background:var(--white);box-shadow:0 2px 8px rgba(0,0,0,.3);padding:4px}
.video-still{width:100%;height:262px;background:linear-gradient(160deg,#1d2c55 0%,#2c4678 35%,#9b7f5a 70%,#c9a77a 100%)}
.video-bar{height:36px;background:linear-gradient(#eeeeee,#d2d2d2);display:flex;align-items:center;gap:12px;padding:0 12px}
.progress{flex:1;height:10px;background:#bdbdbd;border-radius:5px;overflow:hidden}
.progress b{display:block;width:40%;height:100%;background:var(--red)}

/* services */
.services{top:1344px;height:631px;background:var(--panel)}
.service-card{position:absolute;top:185px;width:335px;height:385px;background:var(--white);box-shadow:0 1px 3px rgba(0,0,0,.15)}
.service-photo{height:209px}
.photo-courier{background:linear-gradient(180deg,#385c8c 0%,#c9a07a 55%,#4a3f37 100%)}
.photo-medical{background:linear-gradient(180deg,#e6e8ea 0%,#4d6fa6 60%,#2f4f86 100%)}
.photo-freight{background:linear-gradient(180deg,#6b4a2c 0%,#c9b8a6 50%,#3a5fae 100%)}
.service-badge{position:absolute;left:-15px;top:-15px;width:110px;height:110px;border-radius:50%;background:var(--navy);border:4px solid var(--white);box-shadow:0 0 0 2px var(--navy);color:var(--white);font-weight:700;font-size:17px;line-height:22px;display:flex;align-items:center;justify-content:center;text-align:center}
.service-text{position:absolute;left:20px;top:222px;width:300px;font-size:12px;line-height:18px}
.read-more{position:absolute;left:88px;top:335px;width:159px;height:29px;background:var(--red);border-radius:2px;color:var(--white);font-weight:600;font-size:14px;text-align:center;line-height:29px}

/* testimonials */
.testimonials{top:1975px;height:411px;background:var(--white)}
.avatar{left:95px;top:181px;width:124px;height:124px;border-radius:50%;border:5px solid var(--navy);background:linear-gradient(160deg,#f3e2c5,#e7c9a5);overflow:visible}
.avatar::after{content:"";position:absolute;right:-18px;top:44px;border-left:16px solid var(--navy);border-top:14px solid transparent;border-bottom:14px solid transparent}
.quote-mark{font-family:"Open Sans",sans-serif;font-weight:800;font-size:76px;line-height:1;color:var(--ink)}
.quote-text{left:328px;top:192px;width:780px;font-size:14px;font-weight:700;line-height:22px;color:var(--ink)}
.quote-close{display:inline-block;height:22px;width:40px;margin-left:10px;vertical-align:top;position:relative}
.quote-close::before{content:"\201D";position:absolute;left:0;top:-4px;font-weight:800;font-size:76px;line-height:.8;color:var(--ink)}
.client-name{left:331px;top:284px;font-size:16px;font-style:italic;font-weight:700;color:var(--ink)}
.testimonials .slider-dots{position:absolute;left:562px;top:337px}
.testimonials .slider-dots i{background:var(--white);border:1.5px solid var(--blue)}
.testimonials .slider-dots i.on{background:var(--blue)}

/* footer */
.site-footer{top:2386px;height:293px;background:var(--footer)}
.footer-light{position:absolute;inset:0;background:#f3f3f3;clip-path:polygon(955px 0,1170px 0,1170px 100%,775px 100%)}
.footer-heading{font-size:16px;font-weight:700;color:var(--white);letter-spacing:.3px}
.footer-heading::after{content:"";display:block;height:1px;background:#5b5b5b;margin-top:12px}
.quick-links{left:68px;top:44px;width:110px}
.quick-links ul{list-style:none;margin-top:26px}
.quick-links li{font-size:14px;line-height:21.6px;color:var(--white)}
.contact-block{left:225px;top:44px;width:215px}
.contact-item{display:flex;gap:10px;margin-top:26px;font-size:14px;line-height:21.6px;color:var(--white)}
.contact-item + .contact-item{margin-top:12px}
.contact-item svg{flex:none;margin-top:4px}
.map{left:477px;top:42px;width:300px;height:208px;background:linear-gradient(135deg,#e6e2d7,#d9dcd0 60%,#cfd8c4)}
.site-footer .brand{left:880px;top:128px;gap:8px}
.site-footer .brand-name{font-size:17px}
.site-footer .brand-dot{width:30px;height:30px}
.copyright{position:absolute;left:0;top:2679px;width:1170px;height:31px;background:var(--black);color:var(--white);font-size:11px;font-weight:700;line-height:31px;padding-left:20px}
.social{position:absolute;right:40px;top:7px;display:flex;gap:6px}
.social i{width:18px;height:18px;border-radius:50%;background:var(--white)}
</style>
</head>
<body>
<div class="page">

  <header class="site-header">
    <div class="brand"><span class="brand-name">Brisk Lark Express Delivery</span><span class="brand-dot"></span></div>
    <div class="abs motto-band">ON TIME, ON ROUTE, EVERY LOAD</div>
    <div class="abs phone-icon">
      <svg width="26" height="26" viewBox="0 0 24 24"><path fill="#333" d="M6.6 10.8c1.4 2.8 3.8 5.1 6.6 6.6l2.2-2.2c.3-.3.7-.4 1-.2 1.1.4 2.3.6 3.6.6.6 0 1 .4 1 1V20c0 .6-.4 1-1 1C10.6 21 3 13.4 3 4c0-.6.4-1 1-1h3.5c.6 0 1 .4 1 1 0 1.3.2 2.5.6 3.6.1.3 0 .7-.2 1z"/></svg>
    </div>
    <div class="abs phone-number">1800 555 0142</div>
  </header>

  <nav class="main-nav">
    <a class="active" style="left:216px">HOME</a>
    <a style="left:333px">ABOUT</a>
    <a style="left:426px">COURIER</a>
    <a style="left:534px">MEDICAL</a>
    <a style="left:642px">FREIGHT</a>
    <a style="left:746px">CAREERS</a>
    <a style="left:852px">CONTACT US</a>
  </nav>

  <section class="hero">
    <div class="hero-photo" role="img" aria-label="Photo of a smiling delivery driver with a hand truck of cardboard boxes beside an open white cargo van"></div>
    <div class="slide-arrow prev"><svg width="18" height="22" viewBox="0 0 18 22"><path d="M13 3 5 11l8 8" fill="none" stroke="#fff" stroke-width="3"/></svg></div>
    <div class="slide-arrow next"><svg width="18" height="22" viewBox="0 0 18 22"><path d="m5 3 8 8-8 8" fill="none" stroke="#fff" stroke-width="3"/></svg></div>
    <div class="abs quote-card"></div>
    <div class="abs quote-head">GET INSTANT ONLINE QUOTE</div>
    <div class="abs field" style="top:221px"><div class="icon"><svg width="16" height="16" viewBox="0 0 16 16"><circle cx="8" cy="5" r="3.5" fill="#555"/><path d="M1 16c0-4 3-6 7-6s7 2 7 6z" fill="#555"/></svg></div><span>Name</span></div>
    <div class="abs field" style="top:267px"><div class="icon"><svg width="16" height="16" viewBox="0 0 24 24"><path fill="#555" d="M6.6 10.8c1.4 2.8 3.8 5.1 6.6 6.6l2.2-2.2c.3-.3.7-.4 1-.2 1.1.4 2.3.6 3.6.6.6 0 1 .4 1 1V20c0 .6-.4 1-1 1C10.6 21 3 13.4 3 4c0-.6.4-1 1-1h3.5c.6 0 1 .4 1 1 0 1.3.2 2.5.6 3.6.1.3 0 .7-.2 1z"/></svg></div><span>Mobile Phone</span></div>
    <div class="abs field" style="top:312px"><div class="icon"><svg width="16" height="12" viewBox="0 0 16 12"><rect x=".5" y=".5" width="15" height="11" fill="#555"/><path d="m1 1 7 6 7-6" fill="none" stroke="#ddd" stroke-width="1.4"/></svg></div><span>Email</span></div>
    <div class="abs field" style="top:356px"><div class="icon"><svg width="16" height="16" viewBox="0 0 16 16"><circle cx="8" cy="8" r="7" fill="none" stroke="#555" stroke-width="1.6"/><circle cx="8" cy="8" r="4" fill="none" stroke="#555" stroke-width="1.6"/><circle cx="8" cy="8" r="1.5" fill="#555"/></svg></div><span>Service Needed</span><div class="caret"><svg width="12" height="8" viewBox="0 0 12 8"><path d="M0 0h12L6 8z" fill="#555"/></svg></div></div>
    <div class="abs quote-btn">Get Quote!</div>
    <div class="slider-dots"><i class="on"></i><i></i><i></i><i></i></div>
  </section>

  <section class="welcome">
    <h2 class="section-title">Welcome to Brisk Lark Express Delivery</h2>
    <div class="divider"><i></i></div>
    <div class="abs welcome-copy">
      <p>Lorem ipsum dolor sit amet, consectetuer adipiscing elit, sed diam nonummy nibh euismod tincidunt ut laoreet dolore magna aliquam erat volutpat. Ut wisi enim ad minim veniam, quis nostrud exerci tation ullamcorper suscipit lobortis nisl ut aliquip ex ea commodo consequat.</p>
      <p>Duis autem vel eum iriure dolor in hendrerit in vulputate velit esse molestie consequat, vel illum dolore eu feugiat nulla facilisis at vero eros et accumsan et iusto odio dignissim qui blandit praesent luptatum zzril delenit augue duis dolore te feugait nulla facilisi.</p>
      <p>Nam liber tempor cum soluta nobis eleifend option congue nihil imperdiet doming id quod mazim placerat facer possim assum. Typi non habent claritatem insitam; est usus legentis in iis qui facit eorum claritatem. Investigationes demonstraverunt lectores legere me lius quod ii legunt saepius.</p>
    </div>
    <div class="abs video-frame">
      <div class="video-still" role="img" aria-label="Video still of a courier holding a parcel and clipboard on a city street at dusk"></div>
      <div class="video-bar">
        <svg width="14" height="16" viewBox="0 0 14 16"><path d="M0 0l14 8-14 8z" fill="#777"/></svg>
        <div class="progress"><b></b></div>
        <svg width="18" height="16" viewBox="0 0 18 16"><path d="M0 5h4l5-4v14l-5-4H0z" fill="#777"/><path d="M12 4c2 2 2 6 0 8" fill="none" stroke="#777" stroke-width="1.6"/></svg>
        <svg width="16" height="16" viewBox="0 0 16 16"><path d="M1 1l14 14M15 1 1 15" stroke="#333" stroke-width="2.4"/></svg>
      </div>
    </div>
  </section>

  <section class="services">
    <h2 class="section-title">What We Do</h2>
    <div class="divider"><i></i></div>
    <article class="service-card" style="left:48px">
      <div class="service-photo photo-courier" role="img" aria-label="Photo of cargo being loaded into an aircraft at sunset"></div>
      <div class="service-badge">Express<br>Courier</div>
      <p class="service-text">Lorem ipsum dolor sit amet, consectetuer adipiscing elit, sed diam nonummy nibh euismod tincidunt ut laoreet dolore magna aliquam erat volutpat. Ut wisi enim ad minim veniam, quis nostrud exerci tation ullamcorper suscipit lobortis nisl.</p>
      <div class="read-more">Read more</div>
    </article>
    <article class="service-card" style="left:417px">
      <div class="service-photo photo-medical" role="img" aria-label="Photo of a smiling courier in a blue uniform holding a clipboard"></div>
      <div class="service-badge">Medical<br>Courier</div>
      <p class="service-text">Lorem ipsum dolor sit amet, consectetuer adipiscing elit, sed diam nonummy nibh euismod tincidunt ut laoreet dolore magna aliquam erat volutpat. Ut wisi enim ad minim veniam, quis nostrud exerci tation ullamcorper suscipit lobortis nisl.</p>
      <div class="read-more">Read more</div>
    </article>
    <article class="service-card" style="left:787px">
      <div class="service-photo photo-freight" role="img" aria-label="Photo of a delivery worker handing a package to a customer at a doorway"></div>
      <div class="service-badge">Express<br>Freight</div>
      <p class="service-text">Lorem ipsum dolor sit amet, consectetuer adipiscing elit, sed diam nonummy nibh euismod tincidunt ut laoreet dolore magna aliquam erat volutpat. Ut wisi enim ad minim veniam, quis nostrud exerci tation ullamcorper suscipit lobortis nisl.</p>
      <div class="read-more">Read more</div>
    </article>
  </section>

  <section class="testimonials">
    <h2 class="section-title">Client Testimonials</h2>
    <div class="divider"><i></i></div>
    <div class="abs avatar" role="img" aria-label="Portrait photo of the client"></div>
    <div class="abs quote-mark" style="left:272px;top:172px">&#8221;</div>
    <p class="abs quote-text">Lorem ipsum dolor sit amet, consectetuer adipiscing elit, sed diam nonummy nibh euismod tincidunt ut laoreet dolore magna aliquam erat volu. Wisi enim ad minim veniam, quis nostrud exerci tation ullamcorper suscipit obortis nisl ut aliquip ex ea commodo consequat.<span class="quote-close" aria-hidden="true"></span></p>
    <div class="abs client-name">Marla Fenwick</div>
    <div class="slider-dots"><i class="on"></i><i></i><i></i><i></i></div>
  </section>

  <footer class="site-footer">
    <div class="footer-light"></div>
    <div class="abs quick-links">
      <div class="footer-heading">QUICK LINKS</div>
      <ul><li>Home</li><li>About</li><li>Courier</li><li>Medical</li><li>Freight</li><li>Careers</li><li>Contact</li></ul>
    </div>
    <div class="abs contact-block">
      <div class="footer-heading">CONTACT</div>
      <div class="contact-item"><svg width="11" height="15" viewBox="0 0 11 15"><path d="M5.5 0A5.5 5.5 0 0 0 0 5.5C0 9.5 5.5 15 5.5 15S11 9.5 11 5.5A5.5 5.5 0 0 0 5.5 0z" fill="#e41f2a"/><circle cx="5.5" cy="5.5" r="2" fill="#333"/></svg><span>Brisk Lark Express Delivery<br>48 Harbor Crest Drive<br>Fairview, CA 90299</span></div>
      <div class="contact-item"><svg width="13" height="13" viewBox="0 0 24 24"><path fill="#e41f2a" d="M6.6 10.8c1.4 2.8 3.8 5.1 6.6 6.6l2.2-2.2c.3-.3.7-.4 1-.2 1.1.4 2.3.6 3.6.6.6 0 1 .4 1 1V20c0 .6-.4 1-1 1C10.6 21 3 13.4 3 4c0-.6.4-1 1-1h3.5c.6 0 1 .4 1 1 0 1.3.2 2.5.6 3.6.1.3 0 .7-.2 1z"/></svg><span>1800 555 0142</span></div>
      <div class="contact-item"><svg width="14" height="10" viewBox="0 0 16 12"><rect width="16" height="12" fill="#e41f2a"/><path d="m1 1 7 6 7-6" fill="none" stroke="#333" stroke-width="1.4"/></svg><span>info@brisklark.com</span></div>
    </div>
    <div class="abs map" role="img" aria-label="Street map showing the company location"></div>
    <div class="brand"><span class="brand-name">Brisk Lark Express Delivery</span><span class="brand-dot"></span></div>
  </footer>

  <div class="copyright">COPYRIGHT © 2016 BRISK LARK EXPRESS DELIVERY. ALL RIGHTS RESERVED.
    <div class="social"><i></i><i></i><i></i></div>
  </div>

</div>
</body>
</html>
```